Trelmo redesign

Dorla Fenwick is a CPA specializing in consulting services to veterinarians nationwide. We need to revise the old generalist corporate identity to reflect her specialty. We need a revised card design with a photo of her and the registered trademark slogan The Kennel Ledger Coach(r). The slogan should appear on all materials. The ad needs to be revised with this photo and slogan. Go ahead and use the copy as is. I will revise it later.

Consulting

```html
<!DOCTYPE html>
<html lang="en">
<head>
<meta charset="utf-8">
<title>Trelmo stationery and ad</title>
<link href="https://fonts.googleapis.com/css2?family=Arimo:wght@400;700&family=PT+Sans:wght@400;700&display=swap" rel="stylesheet">
<style>
:root{
  --bg:#d9d9d9;
  --paper:#ffffff;
  --ink:#2b2b2b;
  --grey:#8a8a8a;
  --grey-light:#cfcfcf;
  --grey-mid:#9c9c9c;
  --grey-dark:#5e5e5e;
  --red:#d3232a;
  --shadow:0 4px 14px rgba(0,0,0,.18);
}
*{margin:0;padding:0;box-sizing:border-box}
html,body{width:1200px;height:1000px;overflow:hidden}
body{background:var(--bg);font-family:"Arimo",Arial,sans-serif;color:var(--ink);position:relative}
.sheet{position:absolute;background:var(--paper);box-shadow:var(--shadow);overflow:hidden}

/* identity block */
.brand{display:flex;gap:7px;align-items:flex-start}
.brand-mark{display:flex;align-items:center;gap:4px}
.brand-square{width:12px;height:12px;background:var(--ink)}
.brand-name{font-weight:700;font-size:12px;color:var(--ink)}
.brand-info{font-size:7px;line-height:1.35;color:var(--grey-dark)}
.brand-info .holder{font-weight:700;color:var(--ink);font-size:7.5px}
.brand-info .slogan{color:var(--red)}

.motif{position:absolute;background:linear-gradient(135deg,#fafafa,#e4e4e4)}

/* letterheads */
.letterhead{width:300px;height:388px;top:30px}
.letterhead--classic{left:30px}
.letterhead--classic .brand{position:absolute;left:22px;top:22px}
.letterhead--classic .motif{right:14px;bottom:14px;width:70px;height:70px}
.letterhead--banded{left:350px}
.banded-rule{position:absolute;left:0;right:0;top:36px;height:3px;background:var(--grey-light)}
.letterhead--banded .brand{position:absolute;left:18px;top:22px;background:var(--paper);padding-right:6px}
.offices{position:absolute;left:18px;right:14px;top:68px;display:flex;justify-content:space-between;font-size:5.5px;line-height:1.45;color:var(--grey-dark)}
.banded-foot{position:absolute;left:0;right:0;top:96px;border-top:2px solid var(--grey-light);text-align:right;font-size:5.5px;color:var(--grey);padding:3px 14px 0 0}
.letterhead--banded .motif{right:14px;bottom:14px;width:70px;height:70px}

/* envelopes */
.envelope{width:480px;height:208px;left:690px}
.envelope--front{top:30px}
.envelope--front .brand{position:absolute;left:18px;top:16px}
.envelope--back{top:258px}
.envelope--back .return{position:absolute;right:150px;bottom:22px;font-size:8px;line-height:1.4;color:var(--grey-dark)}
.envelope--back .return .holder{font-weight:700;color:var(--ink);font-size:9px}
.envelope--back .motif{right:16px;bottom:16px;width:110px;height:110px}

/* business cards */
.card{width:280px;height:160px;left:800px}
.card--one{top:500px}
.card--two{top:680px}
.card-band{position:absolute;left:0;right:0;top:42px;height:4px;background:var(--grey-light)}
.card .brand{position:absolute;left:14px;top:14px;background:var(--paper);padding-right:5px}
.card-person{position:absolute;right:16px;top:18px;text-align:right;font-size:9px;color:var(--ink)}
.card-person .title{font-size:7px;color:var(--grey);margin-top:2px}
.card-contact{position:absolute;right:16px;bottom:16px;text-align:right;font-size:6.5px;line-height:1.5;color:var(--grey-dark)}

/* ad */
.ad{left:30px;top:450px;width:730px;height:520px;background:linear-gradient(180deg,#f4f4f4 0%,#d6d6d6 45%,#9a9a9a 100%)}
.ad-headline{position:absolute;left:50px;top:46px;font-size:27px;color:#1f1f1f;font-weight:400;letter-spacing:-.3px}
.ad-wave{position:absolute;left:0;top:0;width:730px;height:520px}
.ad-photo{position:absolute;left:420px;top:110px;width:310px;height:220px;background:linear-gradient(135deg,#e8e8e8,#a9a9a9 60%,#3a3a3a)}
.ad-copy{position:absolute;left:40px;top:320px;width:400px;background:rgba(255,255,255,.28);border-radius:10px;padding:14px 16px;font-family:"PT Sans",sans-serif;font-size:12px;line-height:1.45;color:#fff}
.ad-contact{position:absolute;left:110px;top:478px;font-family:"PT Sans",sans-serif;font-size:12px;color:#fff;letter-spacing:.3px}
.ad-sign{position:absolute;right:34px;bottom:34px;text-align:right;font-family:"PT Sans",sans-serif;color:#fff}
.ad-sign .brand-mark{justify-content:flex-end;margin-bottom:8px}
.ad-sign .brand-square{width:18px;height:18px;background:#1f1f1f}
.ad-sign .brand-name{font-size:18px;color:#1f1f1f}
.ad-sign .holder{font-size:12px;font-weight:700;color:#1f1f1f}
.ad-sign .line{font-size:11px;color:#fff}
</style>
</head>
<body>

<section class="sheet letterhead letterhead--classic">
  <div class="brand">
    <div class="brand-mark"><span class="brand-square"></span><span class="brand-name">Trelmo</span></div>
    <div class="brand-info">
      <div class="holder">Dorla J. Fenwick, CPA, PC</div>
      <div>Certified Public Accountants</div>
      <div class="slogan">The Kennel Ledger Coach®</div>
      <div>1180 North Alder Road, Suite B</div>
      <div>Cedarvale, Ohio 40112</div>
      <div>p 555.014.2270 · f 555.014.2271</div>
      <div>www.trelmo.com</div>
    </div>
  </div>
  <div class="motif" role="img" aria-label="Faint crossing-line motif"></div>
</section>

<section class="sheet letterhead letterhead--banded">
  <div class="banded-rule"></div>
  <div class="brand">
    <div class="brand-mark"><span class="brand-square"></span><span class="brand-name">Trelmo</span></div>
    <div class="brand-info">
      <div class="holder">Dorla J. Fenwick, CPA, PC</div>
      <div>Certified Public Accountants</div>
      <div class="slogan">The Kennel Ledger Coach®</div>
    </div>
  </div>
  <div class="offices">
    <div>1180 North Alder Road, Suite B<br>Cedarvale, Ohio 40112</div>
    <div>p 555.014.2270<br>f 555.014.2271</div>
    <div>66 West Birch Lane<br>Marlow, Ohio 40287</div>
    <div>p 555.014.3380<br>f 555.014.3381</div>
  </div>
  <div class="banded-foot">www.trelmo.com</div>
  <div class="motif" role="img" aria-label="Faint crossing-line motif"></div>
</section>

<section class="sheet envelope envelope--front">
  <div class="brand">
    <div class="brand-mark"><span class="brand-square"></span><span class="brand-name">Trelmo</span></div>
    <div class="brand-info">
      <div class="holder">Dorla J. Fenwick, CPA, PC</div>
      <div>Certified Public Accountants</div>
      <div class="slogan">The Kennel Ledger Coach®</div>
      <div>1180 North Alder Road, Suite B</div>
      <div>Cedarvale, Ohio 40112</div>
    </div>
  </div>
</section>

<section class="sheet envelope envelope--back">
  <div class="return">
    <div class="holder">Dorla J. Fenwick, CPA, PC</div>
    <div>The Kennel Ledger Coach®</div>
    <div>1180 North Alder Road, Suite B</div>
    <div>Cedarvale, Ohio 40112</div>
  </div>
  <div class="motif" role="img" aria-label="Faint crossing-line motif"></div>
</section>

<section class="sheet card card--one">
  <div class="card-band"></div>
  <div class="brand">
    <div class="brand-mark"><span class="brand-square"></span><span class="brand-name">Trelmo</span></div>
    <div class="brand-info">
      <div class="holder">Dorla J. Fenwick, CPA, PC</div>
      <div>Certified Public Accountants</div>
      <div class="slogan">The Kennel Ledger Coach®</div>
    </div>
  </div>
  <div class="card-person" style="top:56px">Dorla J. Fenwick, CPA<div class="title">President</div></div>
  <div class="card-contact">1180 North Alder Road, Suite B<br>Cedarvale, Ohio 40112<br>p 555.014.2270 · f 555.014.2271<br>dorla@trelmo.com · www.trelmo.com</div>
</section>

<section class="sheet card card--two">
  <div class="card-band"></div>
  <div class="brand">
    <div class="brand-mark"><span class="brand-square"></span><span class="brand-name">Trelmo</span></div>
    <div class="brand-info">
      <div class="holder">Dorla J. Fenwick, CPA, PC</div>
      <div>Certified Public Accountants</div>
      <div class="slogan">The Kennel Ledger Coach®</div>
    </div>
  </div>
  <div class="card-person" style="top:56px">Dorla J. Fenwick, CPA<div class="title">President</div></div>
  <div class="card-contact">66 West Birch Lane<br>Marlow, Ohio 40287<br>p 555.014.3380 · f 555.014.3381<br>dorla@trelmo.com · www.trelmo.com</div>
</section>

<section class="sheet ad">
  <h1 class="ad-headline">We go beyond the numbers.</h1>
  <div class="ad-photo" role="img" aria-label="Photo of Dorla Fenwick holding a small black dog"></div>
  <svg class="ad-wave" viewBox="0 0 730 520" aria-hidden="true">
    <path d="M0 170 C150 80 280 110 380 190 C470 260 600 300 730 250 L730 520 L0 520 Z" fill="#8c8c8c"/>
    <path d="M0 170 C150 80 280 110 380 190 C470 260 600 300 730 250 L730 266 C600 316 470 276 380 206 C280 128 150 98 0 186 Z" fill="#1f1f1f"/>
  </svg>
  <p class="ad-copy">If your financial reports leave you wondering how your practice is really doing, we have the answers. Our firm specializes in helping veterinarians get to the true meaning of their financials to set and meet goals for their business and themselves. Of course, we are experts at KVPA financial standards and can show you how your practice compares with others in the state and nationally. Call or email and let us show you what's beyond the numbers.</p>
  <div class="ad-contact">555.014.2270 &nbsp;|&nbsp; dorla@trelmo.com &nbsp;|&nbsp; WWW.TRELMO.COM</div>
  <div class="ad-sign">
    <div class="brand-mark"><span class="brand-square"></span><span class="brand-name">Trelmo</span></div>
    <div class="holder">Dorla J. Fenwick, CPA, PC</div>
    <div class="line">Certified Public Accountants</div>
    <div class="line">The Kennel Ledger Coach®</div>
  </div>
</section>

</body>
</html>
```